Swimming Pool Service business card needed!!!! Please

Hi Everyone! Thanks for looking at my contest. I PROMISE to provide excellent feedback during this process.

I am starting a new swimming pool cleaning business in San Diego, California and would like your help in making a business card for me.

I like easy to read, classy and sophisticated.

I am having a website designed and I'm looking for it to have pictures of really clean & clear pools.

I really like the blue on white color format, but open to other colors.

I do not have a logo, but the name of my company is GLIMMERWAVE POOL SERVICE.

My tag line is: Pools so clean, you can see yourself "in" them. (does not need to have the quotes around "in"...maybe just italics for this word IN?) You decide for me.

I would like to have a logo designed that incorporates some sort of easy to read letters. I do not want cursive (handwriting) letters. I thought about having a "reflection" of letters (mirror image), but think that this will be hard to read from far away. Maybe you can surprise me and come up with an idea that works using the a mirror image....but I'm not sure. I was leaning toward plain old BLOCK letters as I think it would be easy to read on my truck.

I would like to have the NWTBG and HML logos on the back of the card. I have attached those two as files. You can put other things on the back as well, but I need these two logos on there. Or maybe put them on the front of the card if you have a better idea for the back of the card! :-)

Maybe blue on the back of the card and white on the front of the card? I don't know, I'm just thinking out loud.

I had another card done awhile ago called TALLGRASS SHIRTS. I have uploaded a copy of that card for your reference. I don't want this card to be the same as my new company is a swimming pool cleaning company, but I wanted you to see what I liked in the past.

THANK YOU!!!!

Reason: Partner out of town and want their feedback....so need more time to decide and designs still coming in.

Industry/Entity Type

Business

Contact Information for Business Card

GLIMMERWAVE POOL SERVICE
Rick Velund
Owner
8142 Palo Brinco Ave. #219
San Diego, CA 92587
858-291-6037
www.glimmerwavepoolservice.example

Font styles to use
Sans Serif

Colors
0255a3
3176b5
ffffff

Requirements
Nice to have
• Some things to (possibly) add to back of card (in no particular order)
• HML logo
• NWTBG logo
• Free Estimates
• Residential and Commercial Services
• Equipment Repairs
• Saltwater Systems
• Licensed, Bonded, Insured
• Family Owned and Operated
• No Contracts
• =======================
• Check out the FlexMark business card that i attached.
• i think they did this using a chrome overlay.
• Can any of you guys design that? or is that done at my printer?
• ==================
Should not have
• Hi Designers-
• The first round of cards came back and let's stay away from the light blue (powder blue) color. I don't like the look of it on the business cards.
• Also, the pool company JPG's that I attached are other logos of pool companies that I liked. I don't want them to be on my card. The only logos that should be on my card are the one you are going to come up with for my company, the HML logo and the NWTBG logo.
• Lastly, no vertical cards and no split cards (logo on left, contact info on right side).
• Thanks much!

```html
<!DOCTYPE html>
<html lang="en">
<head>
<meta charset="utf-8">
<title>Glimmerwave Pool Service – Business Cards</title>
<link rel="stylesheet" href="https://fonts.googleapis.com/css2?family=Inter:wght@300;400;600;800&family=Ubuntu:ital,wght@0,500;1,500&display=swap">
<style>
  :root {
    --brand-blue: #0a6fd8;
    --deep-blue: #0255a3;
    --ink: #111418;
    --ink-soft: #3a3d42;
    --paper: #ffffff;
    --backdrop: #e9ecef;
    --sky-top: #1e4fb0;
    --sky-low: #6fb1e3;
    --sea: #3fc2c9;
    --pool: #44cfc4;
    --sand: #efe6d6;
  }
  * { margin: 0; padding: 0; box-sizing: border-box; }
  html, body { width: 1200px; height: 1000px; overflow: hidden; }
  body {
    background: var(--backdrop);
    position: relative;
    font-family: "Inter", "Helvetica Neue", Arial, sans-serif;
    color: var(--ink);
  }
  .card {
    position: absolute;
    width: 537px;
    height: 314px;
    background: var(--paper);
    box-shadow: 0 6px 14px rgba(0,0,0,0.18);
    overflow: hidden;
  }
  .card--front { left: 333px; top: 165px; }
  .card--back-left { left: 52px; top: 507px; }
  .card--back-right { left: 616px; top: 507px; }

  .pool-photo {
    position: absolute; inset: 0;
    background: linear-gradient(180deg,
      var(--sky-top) 0%, #3a7fcf 28%, var(--sky-low) 42%,
      var(--sea) 48%, var(--pool) 62%, #2fb3ad 80%,
      var(--sand) 88%, var(--sand) 100%);
  }
  .front-logo {
    position: absolute; left: 128px; top: 24px;
    font-weight: 800;
    color: var(--paper); line-height: 0.95; text-align: right;
  }
  .front-logo .logo-line1 { display: block; font-size: 37px; letter-spacing: 0.5px; }
  .front-logo .logo-line2 { display: block; font-size: 28px; }
  .tagline {
    position: absolute; left: 130px; top: 98px;
    font-family: "Ubuntu", sans-serif; font-weight: 500;
    color: var(--paper); font-size: 14.5px; line-height: 1.05;
  }
  .tagline .indent { padding-left: 4px; }
  .tagline em { font-style: italic; }

  .back-logo {
    position: absolute; top: 27px;
    font-weight: 800; color: var(--brand-blue);
    line-height: 0.95; text-align: right;
  }
  .card--back-left .back-logo { left: 30px; }
  .card--back-right .back-logo { right: 30px; }
  .back-logo .logo-line1 { display: block; font-size: 31px; letter-spacing: 0.3px; }
  .back-logo .logo-line2 { display: block; font-size: 24px; }
  .website {
    position: absolute; top: 97px;
    font-size: 12.5px; color: var(--ink-soft);
  }
  .card--back-left .website { left: 60px; }
  .card--back-right .website { right: 60px; }

  .contact { position: absolute; top: 140px; font-weight: 300; }
  .card--back-left .contact { right: 22px; text-align: right; }
  .card--back-right .contact { left: 21px; text-align: left; }
  .contact .name { font-size: 22px; line-height: 28px; }
  .contact .name b { font-weight: 600; }
  .contact .role { font-size: 17px; line-height: 26px; color: var(--ink-soft); margin-bottom: 12px; }
  .contact .address { font-size: 15px; line-height: 20px; color: var(--ink); }
  .contact .phone { font-size: 15px; line-height: 20px; margin-top: 5px; }
</style>
</head>
<body>

<section class="card card--front">
  <div class="pool-photo" role="img" aria-label="Photo of a crystal-clear infinity pool by the ocean with palm trees, loungers and umbrellas under a blue sky"></div>
  <div class="front-logo">
    <span class="logo-line1">GLIMMERWAVE</span>
    <span class="logo-line2">POOL SERVICE</span>
  </div>
  <p class="tagline">Water so clear,<br><span class="indent">you will want to dive right <em>in</em>.</span></p>
</section>

<section class="card card--back-left">
  <div class="back-logo">
    <span class="logo-line1">GLIMMERWAVE</span>
    <span class="logo-line2">POOL SERVICE</span>
  </div>
  <p class="website">www.glimmerwavepoolservice.example</p>
  <div class="contact">
    <p class="name"><b>Rick</b> Velund</p>
    <p class="role">Owner</p>
    <p class="address">8142 Palo Brinco Ave.<br>#219 San Diego<br>CA 92587</p>
    <p class="phone">Tel: 858 - 291 - 6037</p>
  </div>
</section>

<section class="card card--back-right">
  <div class="back-logo">
    <span class="logo-line1">GLIMMERWAVE</span>
    <span class="logo-line2">POOL SERVICE</span>
  </div>
  <p class="website">www.glimmerwavepoolservice.example</p>
  <div class="contact">
    <p class="name"><b>Rick</b> Velund</p>
    <p class="role">Owner</p>
    <p class="address">8142 Palo Brinco Ave.<br>#219 San Diego<br>CA 92587</p>
    <p class="phone">Tel: 858 - 291 - 6037</p>
  </div>
</section>

</body>
</html>
```